Building company buisness cards

We are looking for a sharp modern new look for our business cards.We are a New Zealand based company that specialises in house and land packages.We have attached a photo of the current logo and would like to see if it can be improved somehow if needed.We are open to any colours but we have chosen Black and White at this stage. Feel free to change the font and make the logo smarter looking.Play with the colours and see what looks best.We want a card that looks so good know one will want to throw it away!

Target Market(s)

Building profesonals, home buyers

Industry/Entity Type

Building

Contact Information for Business Card

Derek Haskins
0274930268
derekh@stonerange.co.nz

Font styles to use
Serif
Sans Serif

Colors

Designer to choose colors to be used in the design.

Requirements
Must have
• Just the logo on one side and details on the other
• Clean simple looking card
Nice to have
• Round corners and detail like raised or spot UV
• Something that stands out
Should not have
• To title needed, Director etc

```html
<!DOCTYPE html>
<html lang="en">
<head>
<meta charset="utf-8">
<title>Stonerange business card</title>
<link rel="stylesheet" href="https://fonts.googleapis.com/css2?family=Crimson+Pro:wght@400;700&display=swap">
<style>
  :root {
    --navy: #1c2758;
    --orange: #ec9923;
    --white: #ffffff;
    --ink-grey: #5a5a5a;
    --backdrop: #e6e6e6;
  }
  * { margin: 0; padding: 0; box-sizing: border-box; }
  html, body {
    width: 1125px; height: 1200px; overflow: hidden;
    background: var(--backdrop);
    font-family: "Crimson Pro", Georgia, serif;
  }
  .card {
    position: absolute; left: 171px; width: 826px; height: 472px;
    border-radius: 26px; overflow: hidden;
  }
  .card--front { top: 106px; background: var(--white); }
  .card--back { top: 639px; background: var(--navy); }

  .brand {
    position: absolute; top: 88px; left: 0; width: 100%;
    text-align: center;
    font-size: 76px; font-weight: 700; color: var(--navy);
    line-height: 1; letter-spacing: 0;
  }

  .name-band {
    position: absolute; top: 276px; left: 0; width: 100%; height: 52px;
    background: var(--orange);
  }
  .name-band svg { position: absolute; inset: 0; }
  .name-band__text {
    position: absolute; inset: 0;
    display: flex; align-items: center; justify-content: center;
    color: var(--white); font-weight: 700; font-size: 30px;
    letter-spacing: 0.5px; text-transform: uppercase;
  }

  .contact {
    position: absolute; top: 372px; left: 0; width: 100%;
    text-align: center; color: var(--ink-grey); font-size: 19px; line-height: 1.4;
  }
  .contact__web {
    color: var(--navy); letter-spacing: 2.5px; font-size: 19px;
  }

  .back__texture {
    position: absolute; inset: 0;
    background: radial-gradient(circle at 30% 30%, #24306a 0%, var(--navy) 70%);
  }
  .back__name {
    position: absolute; right: 58px; bottom: 82px;
    color: var(--white); font-size: 24px; font-weight: 700;
  }
</style>
</head>
<body>
  <section class="card card--front">
    <div class="brand">Stonerange</div>
    <div class="name-band">
      <svg width="826" height="52" viewBox="0 0 826 52">
        <polygon points="188,0 653,0 640,52 172,52" fill="#ffffff"/>
        <polygon points="192,0 651,0 637,52 177,52" fill="#1c2758"/>
      </svg>
      <div class="name-band__text">Derek Haskins</div>
    </div>
    <div class="contact">
      <p>Phone : 0274930268 |&nbsp; derekh@stonerange.co.nz</p>
      <p class="contact__web">www.stonerange.co.nz</p>
    </div>
  </section>

  <section class="card card--back">
    <div class="back__texture" role="img" aria-label="Faint repeating brand pattern texture"></div>
    <div class="back__name">Stonerange</div>
  </section>
</body>
</html>
```